Blitz Handouts

I need to design a leave behind or handout that can be left with clients. This will be for a property blitz and for trade shows. I want them about the size of a post card. I want them to go along with our current theme from our website and our social media. I have attached pictures of our new logos. I have also attached a picture of my business card to show the things we provide. website https://maplecrestbld.com/the-company/ Please use the email tbrandow@maplecrestbld.com 555.208.4163

```html
<!DOCTYPE html>
<html lang="en">
<head>
<meta charset="utf-8">
<title>Maplecrest Builders – Blitz Handout</title>
<link rel="stylesheet" href="https://fonts.googleapis.com/css2?family=Anton&family=Montserrat:wght@400;500;600;700&display=swap">
<style>
  :root {
    --page: #dcdcdc;
    --navy: #14315f;
    --navy-deep: #0f2648;
    --blue: #2460a7;
    --blue-light: #3b7cc4;
    --white: #ffffff;
    --ink: #2a2a2a;
    --rule: #9a9a9a;
  }
  * { margin: 0; padding: 0; box-sizing: border-box; }
  html, body { width: 1113px; height: 1200px; overflow: hidden; background: var(--page); }
  .sheet { position: relative; width: 1113px; height: 1200px; }
  .card {
    position: absolute; left: 176px; width: 760px; height: 540px;
    background: var(--white); overflow: hidden;
    box-shadow: 0 3px 8px rgba(0,0,0,.35);
    font-family: "Montserrat", sans-serif;
  }
  .card--front { top: 40px; }
  .card--back { top: 620px; }
  .card__art { position: absolute; inset: 0; width: 760px; height: 540px; }
  .abs { position: absolute; }

  /* brand */
  .brand { display: flex; align-items: center; gap: 12px; }
  .brand__mark { background: var(--blue); border: 3px solid var(--white); }
  .brand__name { font-weight: 700; color: var(--white); line-height: 1; }
  .brand__sub { font-weight: 700; color: var(--white); letter-spacing: 5px; font-size: 11px; margin-top: 4px; }
  .card--front .brand { left: 32px; top: 34px; }
  .card--front .brand__mark { width: 66px; height: 66px; }
  .card--front .brand__name { font-size: 34px; }

  /* front */
  .services-tag {
    left: 32px; top: 156px; width: 157px; height: 37px;
    background: var(--blue); border: 2px solid var(--blue-light); border-radius: 6px;
    font-family: "Anton", sans-serif; color: var(--white); font-size: 22px;
    display: flex; align-items: center; justify-content: center; letter-spacing: .3px;
  }
  .services { left: 210px; top: 125px; list-style: none; }
  .services li {
    color: var(--white); font-weight: 600; font-size: 15.5px; line-height: 21px;
  }
  .services li::before { content: "\25C6"; font-size: 9px; margin-right: 5px; vertical-align: 2px; }
  .headline {
    left: 376px; top: 10px; width: 364px; text-align: right;
    font-family: "Anton", sans-serif; color: var(--white); font-size: 34px; line-height: 50px; letter-spacing: .3px;
  }
  .story {
    left: 382px; top: 84px; width: 356px;
    font-size: 11.2px; line-height: 14.8px; color: var(--ink); text-align: justify; text-align-last: center;
  }
  .phone {
    right: 26px; top: 350px; font-family: "Anton", sans-serif; color: var(--white);
    font-size: 70px; line-height: 86px;
  }
  .email { right: 26px; top: 438px; color: var(--white); font-size: 27px; font-weight: 500; }
  .web { right: 26px; top: 487px; color: var(--navy); font-size: 37px; font-weight: 700; line-height: 44px; }

  /* back */
  .welcome {
    left: 34px; top: 62px; color: var(--white); font-size: 25px; font-weight: 600; line-height: 31px;
  }
  .intro {
    left: 34px; top: 130px; width: 340px; color: var(--white);
    font-size: 13.4px; line-height: 18.6px; font-weight: 500;
  }
  .card--back .brand { left: 436px; top: 30px; gap: 10px; }
  .card--back .brand__mark { width: 44px; height: 52px; border-color: var(--navy); }
  .card--back .brand__name { font-size: 22px; color: var(--blue); }
  .card--back .brand__sub { color: var(--blue); font-size: 8px; letter-spacing: 3.4px; margin-top: 2px; }
  .stamp { left: 671px; top: 21px; width: 74px; height: 72px; border: 1px solid var(--rule); }
  .address-line { left: 450px; width: 281px; height: 0; border-top: 1px solid var(--rule); }
</style>
</head>
<body>
<div class="sheet">

  <!-- Front of handout -->
  <section class="card card--front">
    <svg class="card__art" viewBox="0 0 760 540" aria-hidden="false">
      <defs>
        <linearGradient id="navyPanel" x1="0" y1="0" x2="0" y2="1">
          <stop offset="0" stop-color="#14315f"/>
          <stop offset=".5" stop-color="#1c4a8a"/>
          <stop offset="1" stop-color="#14315f"/>
        </linearGradient>
        <linearGradient id="headerBand" x1="0" y1="0" x2="1" y2="0">
          <stop offset="0" stop-color="#14315f"/>
          <stop offset="1" stop-color="#3b7cc4"/>
        </linearGradient>
        <linearGradient id="buildingPhoto" x1="0" y1="0" x2="0" y2="1">
          <stop offset="0" stop-color="#2f63a8"/>
          <stop offset=".35" stop-color="#6b5a4c"/>
          <stop offset=".75" stop-color="#8a6a52"/>
          <stop offset="1" stop-color="#55504c"/>
        </linearGradient>
      </defs>
      <path d="M0 0H338L366 44V350C366 430 300 470 190 505L95 540H0Z" fill="url(#navyPanel)"/>
      <path d="M0 215C130 215 290 230 366 262V350C366 430 300 470 190 505L95 540H0Z" fill="url(#buildingPhoto)" role="img" aria-label="Photo of a row of modern multifamily townhomes under a blue sky"/>
      <path d="M366 44V350C366 430 300 470 190 505L95 540" fill="none" stroke="#2460a7" stroke-width="5"/>
      <path d="M108 0C150 30 280 30 322 0Z" fill="#ffffff"/>
      <path d="M340 0H760V71H372Z" fill="url(#headerBand)"/>
      <rect x="366" y="344" width="394" height="139" fill="#14315f"/>
      <path d="M366 344H760V483H250C320 450 366 410 366 344Z" fill="#14315f"/>
    </svg>

    <div class="abs brand">
      <span class="brand__mark"></span>
      <div>
        <div class="brand__name">MAPLECREST</div>
        <div class="brand__sub">BUILDERS</div>
      </div>
    </div>

    <div class="abs services-tag">OUR SERVICES</div>
    <ul class="abs services">
      <li>ROOFING</li>
      <li>PAINTING</li>
      <li>CARPENTRY</li>
      <li>WELDING</li>
      <li>GUTTERS</li>
      <li>CONCRETE</li>
      <li>COMMERCIAL</li>
    </ul>

    <h1 class="abs headline">MAPLECREST BUILDERS</h1>
    <p class="abs story">Founded in 2002 by Dale Ferris, Maplecrest Builders is a business with family at its core. Maplecrest was created with a shield in its logo to represent the guarding of the families working for the company as well as those they serve. In 2014, Owen Rudd joined the Maplecrest family as partner to Dale thus expanding the business and furthering its growth. Having now grown into a National company with Territory Offices in 7 states and representation of work in 15 with continued expansion, Maplecrest is still a family business at heart. The company offers a variety of construction solutions for both the commercial and multifamily industries. The focus is on building long-term relationships with clientele that are based on both trust and integrity. Clients can count on Maplecrest Builders to complete projects in a professional and timely manner with attention to detail that meets the “Maplecrest Standard” and stands strong with the shield.</p>

    <div class="abs phone">555.208.4163</div>
    <div class="abs email">tbrandow@maplecrestbld.com</div>
    <div class="abs web">www.maplecrestbld.com</div>
  </section>

  <!-- Back of handout -->
  <section class="card card--back">
    <svg class="card__art" viewBox="0 0 760 540">
      <defs>
        <linearGradient id="backPanel" x1="0" y1="0" x2="1" y2="1">
          <stop offset="0" stop-color="#14315f"/>
          <stop offset=".6" stop-color="#1c4a8a"/>
          <stop offset="1" stop-color="#2460a7"/>
        </linearGradient>
        <linearGradient id="brickPhoto" x1="0" y1="0" x2="0" y2="1">
          <stop offset="0" stop-color="#b9bcc2"/>
          <stop offset=".45" stop-color="#7a5d4e"/>
          <stop offset="1" stop-color="#9a9690"/>
        </linearGradient>
        <linearGradient id="playPhoto" x1="0" y1="0" x2="0" y2="1">
          <stop offset="0" stop-color="#b8b3ad"/>
          <stop offset=".5" stop-color="#8a5a3e"/>
          <stop offset="1" stop-color="#4f7a3a"/>
        </linearGradient>
        <linearGradient id="interiorPhoto" x1="0" y1="0" x2="0" y2="1">
          <stop offset="0" stop-color="#3a3a3e"/>
          <stop offset=".4" stop-color="#e6e8ea"/>
          <stop offset="1" stop-color="#8a7a70"/>
        </linearGradient>
      </defs>
      <path d="M0 0H390L418 40V360C418 440 360 480 300 505L230 540H0Z" fill="url(#backPanel)"/>
      <path d="M418 40V360C418 440 360 480 300 505L230 540" fill="none" stroke="#3b7cc4" stroke-width="5"/>
      <path d="M160 0C200 30 340 30 378 0Z" fill="#ffffff"/>
      <polygon points="24,385 78,291 186,291 240,385 186,479 78,479" fill="url(#brickPhoto)" stroke="#ffffff" stroke-width="4" role="img" aria-label="Photo of a single-storey brick building"/>
      <polygon points="233,341 260,294 314,294 341,341 314,388 260,388" fill="url(#playPhoto)" stroke="#ffffff" stroke-width="4" role="img" aria-label="Photo of a red playground on wood chips"/>
      <polygon points="226,466 263,401 339,401 376,466 339,531 263,531" fill="url(#interiorPhoto)" stroke="#ffffff" stroke-width="4" role="img" aria-label="Photo of a bright vaulted clubhouse interior"/>
    </svg>

    <h2 class="abs welcome">WELCOME TO<br>MAPLECREST BUILDERS</h2>
    <p class="abs intro">Founded in 2002, Maplecrest Builders offers a variety of construction solutions for both the commercial and multifamily industries. With a focus on building long-term relationships, our clients can count on the Maplecrest Builders team to complete projects in a professional and timely manner with an attention to detail that stands strong with our standards.</p>

    <div class="abs brand">
      <span class="brand__mark"></span>
      <div>
        <div class="brand__name">MAPLECREST</div>
        <div class="brand__sub">BUILDERS</div>
      </div>
    </div>
    <div class="abs stamp"></div>
    <div class="abs address-line" style="top:264px"></div>
    <div class="abs address-line" style="top:307px"></div>
    <div class="abs address-line" style="top:351px"></div>
    <div class="abs address-line" style="top:394px"></div>
  </section>

</div>
</body>
</html>
```